Website Landing Page for Brightfall Systems

Create a custom designed website landing page for our business. Looking for a professional upscale design that incorporates our logo and logo colors into the theme. I want a standard fixed frame website, not a constant scrolling format that seems to be the trend. To start with I'm looking for more of the graphic design part, maybe a concept or theme, I don't expect to see a finished project. Not interested in generic templates or layouts.

The name of our company is Brightfall Systems and I've attached our logo below. I'd like to have the web page have the same look and feel of our logo, as well as the colors. Our company, Brightfall Systems does system design, installation, and programming, of residential and commercial Audio/Video and Automation systems. We do home theaters, lighting and building automation, video conferencing systems, security camera installations, conference rooms, projectors, distributed audio systems, and similar Technology projects. This will be a professional services/informational website. We will not sell products on this website. This website will be used to advertise our company and communicate our services to prospective customers. Having a well designed, professional and clean website is one way we want to distinguish our company from the competition.

Here are some examples of what I consider a professional well designed website
http://www.qorlamstudio.com/Work/

Last year we had our tradlo store designed (with PixelMarket) and I'm really happy with the way it turned out. You can see it at www.HolvenGearDepot.com I consider this to be a great design and looking for the same level of quality with this new website. However, do not copy or use any part of this design in this new project. This tradlo store is completely separate from our other company Brightfall Systems. I only mention this tradlo store an an example of good work.

Reason: Still going through designs.

Reason: Still working on project and have not had time to review all designs and request revisions.

Reason: Sill going through designs and requesting revisions

Reason: still going through all the submissions we received.

Target Market(s)

People interested in Audio/Video, home theaters, home automation. We do sales, system design, and programming. We typically work on larger projects with both residential and commercial customers.

Industry/Entity Type

Business

Number of Pages Required

1 page

Requirements
Must have
• Great design elements. Please use a white background. I think white goes well with our logo colors.

```html
<!DOCTYPE html>
<html lang="en">
<head>
<meta charset="utf-8">
<title>Brightfall Systems</title>
<link href="https://fonts.googleapis.com/css2?family=Oswald:wght@400;500&family=Lato:wght@400&display=swap" rel="stylesheet">
<style>
:root{
  --blue:#3a9fdd;
  --blue-mid:#3585cc;
  --blue-deep:#1d5ca8;
  --green:#7cc540;
  --green-bright:#9bd845;
  --green-dark:#5aa632;
  --panel:#eef0f2;
  --panel-edge:#e3e6e9;
  --ink:#3b3b3b;
  --muted:#6d6d6d;
  --white:#ffffff;
}
*{box-sizing:border-box;margin:0;padding:0}
html,body{width:1200px;height:2250px;overflow:hidden;background:var(--white)}
.page{position:relative;width:1200px;height:2250px;overflow:hidden;background:var(--white);font-family:'Oswald',sans-serif;color:var(--ink)}
.abs{position:absolute}
.photo{position:absolute}

/* header */
.brand{position:absolute;left:142px;top:52px;display:flex;align-items:center;gap:18px}
.brand-mark{width:78px;height:78px;border-radius:50%;border:7px solid var(--blue)}
.brand-name{font-size:33px;line-height:36px;font-weight:500;color:var(--blue);letter-spacing:1px;text-transform:uppercase}
.search{position:absolute;left:507px;top:57px;width:186px;height:24px;border-radius:12px;background:#d4d6d8;font-family:'Lato',sans-serif;font-size:11px;color:#f5f5f5;padding:5px 12px}
.search svg{position:absolute;right:9px;top:5px}
.social{position:absolute;left:508px;top:98px;display:flex;gap:11px}
.social span{width:28px;height:28px;border-radius:50%;background:#c9cbcd}

/* hero */
.welcome{position:absolute;right:30px;top:344px;text-align:right;color:var(--white);text-transform:uppercase;font-weight:500;line-height:1}
.welcome .small{font-size:34px}
.welcome .big{font-size:66px;margin-top:10px}
.welcome .mid{font-size:42px;margin-top:10px}

/* highlights */
.highlights-panel{position:absolute;left:0;top:567px;width:1200px;height:330px;background:var(--panel)}
.promise-banner{position:absolute;left:112px;top:570px;width:976px;height:48px;color:var(--white);font-size:29px;font-weight:500;text-align:center;line-height:48px;text-transform:uppercase}
.service-link{position:absolute;display:flex;align-items:center;gap:22px;font-size:19px;line-height:24px;text-transform:uppercase;color:var(--ink)}
.perk{position:absolute;display:flex;align-items:center;gap:16px;font-size:20px;line-height:26px;text-transform:uppercase;color:var(--ink)}
.contact-bar{position:absolute;left:397px;top:835px;width:540px;height:42px;color:var(--white);font-size:19px;text-transform:uppercase;line-height:42px;text-align:center}

/* services */
.service-label{position:absolute;top:1126px;width:200px;text-align:center;color:var(--green-dark);font-size:20px;font-weight:500;text-transform:uppercase}

/* expertise */
.cat-title{position:absolute;left:126px;top:1196px;color:var(--white);font-size:31px;font-weight:500;text-transform:uppercase}
.cat{position:absolute;width:250px;text-align:center;color:var(--white);font-size:29px;text-transform:uppercase;line-height:1;white-space:nowrap}
.cat svg{display:block;margin:0 auto 14px}

/* venues */
.venue-label{position:absolute;height:47px;line-height:47px;color:var(--white);font-size:25px;font-weight:500;text-transform:uppercase;text-align:center}
.venue-brand{position:absolute;left:450px;top:1720px;width:300px;text-align:center}
.venue-brand .ring{width:120px;height:120px;border-radius:50%;border:10px solid var(--blue);margin:0 auto 18px}
.venue-brand .name{font-size:27px;line-height:30px;font-weight:500;color:var(--blue);text-transform:uppercase}

/* footer */
.disclaimer{position:absolute;left:200px;top:2102px;width:800px;text-align:center;font-family:'Lato',sans-serif;font-size:13px;line-height:18px;color:var(--muted)}
.footer-rule{position:absolute;left:210px;top:2160px;width:780px;height:1px;background:#e2e2e2}
.footer-nav{position:absolute;left:0;top:2176px;width:1200px;text-align:center;font-family:'Lato',sans-serif;font-size:16px;color:#555;text-transform:uppercase}
.footer-nav span{margin:0 10px}
.copyright{position:absolute;left:0;top:2204px;width:1200px;text-align:center;font-family:'Lato',sans-serif;font-size:14px;color:var(--blue)}
.bottom-bar{position:absolute;left:0;top:2238px;width:1200px;height:12px;background:var(--blue)}
</style>
</head>
<body>
<div class="page">

  <!-- header & hero shapes -->
  <div class="photo" role="img" aria-label="Photo of a modern living room wall paneling" style="left:680px;top:0;width:420px;height:165px;background:linear-gradient(135deg,#6b4b3a,#b08a6c 55%,#3e2e26);clip-path:polygon(60px 0,420px 0,390px 165px,0 165px)"></div>
  <div class="photo" role="img" aria-label="Photo of a living room with a large wall screen showing a waterfall" style="left:0;top:165px;width:1060px;height:383px;background:linear-gradient(160deg,#c8b79a 0%,#e8dcc4 35%,#8a6a4d 65%,#b9a282 100%)"></div>

  <svg class="abs" style="left:0;top:0" width="1200" height="548" viewBox="0 0 1200 548">
    <polygon points="0,0 150,0 0,150" fill="var(--green)"/>
    <polygon points="150,0 200,0 0,200 0,150" fill="var(--green-bright)" opacity=".55"/>
    <polygon points="1090,0 1200,0 1200,14 1100,14" fill="var(--green)"/>
    <polygon points="1085,86 1170,86 1127,128" fill="var(--green-bright)" opacity=".8"/>
    <polygon points="1200,90 745,548 1200,548" fill="var(--blue)"/>
    <polygon points="1200,150 820,548 1200,548" fill="var(--blue-mid)" opacity=".45"/>
    <polygon points="640,262 720,262 680,222" fill="#ffffff" opacity=".35"/>
    <polygon points="745,480 860,480 800,548" fill="var(--green)" opacity=".75"/>
    <polygon points="1040,165 1200,165 1200,190" fill="#ffffff" opacity=".4"/>
  </svg>

  <div class="brand">
    <div class="brand-mark"></div>
    <div class="brand-name">Brightfall<br>Systems</div>
  </div>
  <div class="search">Search
    <svg width="14" height="14" viewBox="0 0 14 14"><circle cx="8" cy="6" r="4" fill="none" stroke="#fff" stroke-width="1.6"/><line x1="5" y1="9" x2="1" y2="13" stroke="#fff" stroke-width="1.6"/></svg>
  </div>
  <div class="social"><span></span><span></span><span></span><span></span><span></span></div>

  <div class="welcome">
    <div class="small">Welcome to</div>
    <div class="big">Brightfall</div>
    <div class="mid">Systems</div>
  </div>

  <!-- highlights -->
  <div class="highlights-panel"></div>
  <svg class="abs" style="left:0;top:567px" width="1200" height="330" viewBox="0 0 1200 330">
    <polygon points="0,0 112,0 0,170" fill="var(--green)"/>
    <polygon points="0,170 112,0 130,0 0,200" fill="var(--green-bright)" opacity=".6"/>
    <polygon points="505,70 540,70 450,250 415,250" fill="#ffffff" opacity=".6"/>
    <polygon points="112,3 1088,3 1068,51 128,51" fill="var(--blue)"/>
    <polygon points="410,268 937,268 920,310 397,310" fill="var(--green)"/>
  </svg>
  <div class="photo" role="img" aria-label="Photo of a glass office tower seen from below" style="left:935px;top:567px;width:265px;height:330px;background:linear-gradient(160deg,#7fb2de,#2d5f93 55%,#a9c7e3);clip-path:polygon(60px 0,265px 0,265px 330px,0 330px)"></div>
  <div class="promise-banner">Design, Installation &amp; Programming Done Right</div>

  <div class="service-link" style="left:160px;top:645px">
    <svg width="80" height="70" viewBox="0 0 80 70"><polygon points="0,0 80,0 40,70" fill="var(--blue-deep)"/><path d="M40 12 L52 17 V28 C52 36 46 41 40 44 C34 41 28 36 28 28 V17 Z" fill="none" stroke="var(--green-bright)" stroke-width="2.5"/><path d="M34 28 L39 33 L47 23" fill="none" stroke="var(--green-bright)" stroke-width="2.5"/></svg>
    <span>Service &amp; Support</span>
  </div>
  <div class="service-link" style="left:118px;top:725px">
    <svg width="80" height="70" viewBox="0 0 80 70"><polygon points="0,0 80,0 40,70" fill="var(--blue-deep)"/><rect x="25" y="10" width="30" height="22" fill="none" stroke="var(--green-bright)" stroke-width="2.5"/><line x1="25" y1="16" x2="55" y2="16" stroke="var(--green-bright)" stroke-width="2"/><text x="40" y="29" fill="var(--green-bright)" font-size="9" text-anchor="middle" font-family="Lato,sans-serif">&lt;/&gt;</text></svg>
    <span>System Design &amp;<br>Programming</span>
  </div>
  <div class="service-link" style="left:74px;top:800px">
    <svg width="80" height="70" viewBox="0 0 80 70"><polygon points="0,0 80,0 40,70" fill="var(--blue-deep)"/><path d="M26 30 L40 16 L54 30 M30 26 V40 H50 V26" fill="none" stroke="var(--green-bright)" stroke-width="2.5"/></svg>
    <span>Projects We Build</span>
  </div>

  <div class="perk" style="left:540px;top:648px">
    <svg width="48" height="56" viewBox="0 0 48 56"><circle cx="24" cy="12" r="10" fill="var(--green-dark)"/><rect x="18" y="20" width="12" height="14" fill="var(--green-dark)"/><rect x="4" y="34" width="40" height="10" rx="2" fill="var(--green-dark)"/><rect x="2" y="48" width="44" height="5" fill="var(--green-dark)"/></svg>
    <span>Certified<br>Integrator</span>
  </div>
  <div class="perk" style="left:798px;top:645px">
    <svg width="64" height="58" viewBox="0 0 64 58"><rect x="2" y="2" width="54" height="44" fill="none" stroke="var(--green-dark)" stroke-width="3"/><line x1="2" y1="12" x2="56" y2="12" stroke="var(--green-dark)" stroke-width="3"/><path d="M22 22 L50 52 M50 22 L22 52" stroke="var(--green-dark)" stroke-width="5" stroke-linecap="round"/></svg>
    <span>Expert Tech<br>Support</span>
  </div>
  <div class="perk" style="left:490px;top:745px">
    <svg width="54" height="54" viewBox="0 0 54 54"><path d="M4 4 H50 V38 H22 L10 50 V38 H4 Z" fill="var(--green-dark)"/><path d="M14 16 H40 M14 26 H32" stroke="#fff" stroke-width="3"/></svg>
    <span>Free<br>Consultation</span>
  </div>
  <div class="perk" style="left:740px;top:744px">
    <svg width="70" height="70" viewBox="0 0 70 70"><circle cx="35" cy="35" r="32" fill="none" stroke="var(--green-dark)" stroke-width="3"/><circle cx="35" cy="35" r="22" fill="none" stroke="var(--green-dark)" stroke-width="2"/><path d="M25 36 L32 43 L46 28" fill="none" stroke="var(--green-dark)" stroke-width="3.5"/></svg>
    <span>Custom<br>Solutions</span>
  </div>
  <div class="contact-bar">Planning a project? Contact us for a consultation!</div>

  <!-- services -->
  <svg class="abs" style="left:0;top:900px" width="1200" height="285" viewBox="0 0 1200 285">
    <path d="M0 150 C200 60 300 200 480 110" fill="none" stroke="#d9dcdf" stroke-width="1.5"/>
    <path d="M0 165 C220 80 320 210 480 125" fill="none" stroke="#e3e5e8" stroke-width="1.5"/>
    <path d="M720 110 C900 200 1000 60 1200 150" fill="none" stroke="#d9dcdf" stroke-width="1.5"/>
    <path d="M720 125 C900 210 1000 80 1200 165" fill="none" stroke="#e3e5e8" stroke-width="1.5"/>
    <g fill="none" stroke="var(--green)" stroke-width="2.5">
      <polygon points="240,80 420,80 330,215"/>
      <polygon points="522,80 702,80 612,215"/>
      <polygon points="792,80 972,80 882,215"/>
    </g>
    <g fill="var(--blue-deep)">
      <polygon points="330,30 420,183 240,183"/>
      <polygon points="612,30 702,183 522,183"/>
      <polygon points="882,30 972,183 792,183"/>
    </g>
    <g stroke="#fff" stroke-width="4" fill="none" stroke-linecap="round">
      <path d="M298 160 V142 M312 160 V132 M326 160 V122 M340 160 V112"/>
      <path d="M296 138 L340 104 M330 104 H340 V114"/>
      <rect x="584" y="104" width="56" height="40"/>
      <path d="M604 154 H620 M612 144 V154"/>
      <path d="M598 134 L618 114 L624 118"/>
      <rect x="854" y="104" width="56" height="40"/>
      <path d="M874 154 H890 M882 144 V154"/>
    </g>
    <text x="330" y="101" fill="#fff" font-size="20" font-weight="500" text-anchor="middle" font-family="Oswald,sans-serif">$</text>
    <text x="882" y="131" fill="#fff" font-size="18" text-anchor="middle" font-family="Oswald,sans-serif">&lt;/&gt;</text>
  </svg>
  <div class="service-label" style="left:230px">Sales</div>
  <div class="service-label" style="left:512px">System Design</div>
  <div class="service-label" style="left:782px">Programming</div>

  <!-- expertise -->
  <svg class="abs" style="left:0;top:1185px" width="1200" height="420" viewBox="0 0 1200 420">
    <rect x="0" y="0" width="1200" height="60" fill="var(--green)"/>
    <polygon points="110,0 300,0 290,60 100,60" fill="var(--green-bright)"/>
    <rect x="0" y="60" width="1200" height="168" fill="var(--blue)"/>
    <rect x="0" y="228" width="1200" height="165" fill="var(--blue-mid)"/>
    <polygon points="0,60 80,60 0,230" fill="var(--green)"/>
    <polygon points="1200,210 1200,393 1105,393" fill="var(--green)"/>
    <g stroke="#ffffff" stroke-opacity=".45" stroke-width="2" fill="none">
      <path d="M400 60 L345 228 L400 393"/>
      <path d="M653 60 L598 228 L653 393"/>
      <path d="M903 60 L848 228 L903 393"/>
      <line x1="0" y1="228" x2="1200" y2="228"/>
    </g>
    <rect x="0" y="400" width="760" height="14" fill="var(--blue)"/>
    <rect x="770" y="400" width="430" height="14" fill="var(--blue)"/>
  </svg>
  <div class="cat-title">Expertise</div>

  <div class="cat" style="left:93px;top:1292px">
    <svg width="56" height="54" viewBox="0 0 56 54" fill="none" stroke="#fff" stroke-width="3.5"><path d="M4 20 H52 L46 50 H10 Z"/><path d="M14 20 L28 4 L42 20"/><path d="M28 28 V42 M21 35 H35"/></svg>All Services</div>
  <div class="cat" style="left:368px;top:1288px">
    <svg width="60" height="58" viewBox="0 0 60 58" fill="none" stroke="#fff" stroke-width="3"><circle cx="30" cy="22" r="9"/><path d="M26 24 V46 C26 52 34 56 44 52 V36 L30 32" stroke-linejoin="round"/><path d="M8 22 L14 16 M8 22 L14 28 M52 22 L46 16 M52 22 L46 28 M30 2 V8"/></svg>Automation</div>
  <div class="cat" style="left:610px;top:1286px">
    <svg width="50" height="62" viewBox="0 0 50 62" fill="#fff"><rect x="4" y="2" width="10" height="10"/><rect x="20" y="2" width="10" height="10"/><rect x="36" y="2" width="10" height="10"/><rect x="4" y="16" width="10" height="10"/><rect x="36" y="16" width="10" height="10"/><path d="M20 20 H30 V40 L40 38 V58 H22 L14 44 L20 42 Z"/></svg>Lighting</div>
  <div class="cat" style="left:862px;top:1286px">
    <svg width="60" height="60" viewBox="0 0 60 60" fill="none" stroke="#fff" stroke-width="3.5"><rect x="6" y="30" width="48" height="26"/><rect x="12" y="6" width="36" height="18"/><line x1="30" y1="24" x2="30" y2="30"/><path d="M14 40 H22 M26 40 H34 M38 40 H46 M14 48 H46"/></svg>Control Systems</div>

  <div class="cat" style="left:97px;top:1457px">
    <svg width="72" height="56" viewBox="0 0 72 56" fill="none" stroke="#fff" stroke-width="3.5"><rect x="30" y="2" width="36" height="50" rx="3"/><rect x="4" y="20" width="40" height="24" rx="3" fill="var(--blue-mid)"/><line x1="4" y1="28" x2="44" y2="28"/></svg>Conferencing</div>
  <div class="cat" style="left:385px;top:1455px">
    <svg width="66" height="58" viewBox="0 0 66 58" fill="#fff"><path d="M4 4 H50 V40 H4 Z" fill="none" stroke="#fff" stroke-width="3.5"/><rect x="20" y="46" width="14" height="6"/><rect x="44" y="6" width="7" height="7"/><rect x="54" y="12" width="7" height="7"/><rect x="46" y="20" width="7" height="7"/><rect x="56" y="26" width="7" height="7"/><rect x="40" y="30" width="7" height="7"/></svg>Projectors</div>
  <div class="cat" style="left:645px;top:1462px">
    <svg width="80" height="48" viewBox="0 0 80 48" fill="#fff"><rect x="2" y="4" width="52" height="40" rx="4"/><polygon points="56,24 78,6 78,42"/><circle cx="16" cy="24" r="8" fill="var(--blue-mid)"/><circle cx="38" cy="24" r="8" fill="var(--blue-mid)"/></svg>Security Cameras</div>
  <div class="cat" style="left:866px;top:1455px">
    <svg width="52" height="58" viewBox="0 0 52 58" fill="#fff"><rect x="4" y="2" width="44" height="14"/><rect x="4" y="20" width="44" height="14"/><rect x="4" y="38" width="30" height="16"/><circle cx="40" cy="46" r="10" fill="none" stroke="#fff" stroke-width="4"/></svg>Distributed Audio</div>

  <!-- venues -->
  <svg class="abs" style="left:0;top:1612px" width="1200" height="460" viewBox="0 0 1200 460">
    <rect x="0" y="0" width="1200" height="460" fill="var(--panel)"/>
    <polygon points="600,0 860,230 600,460 340,230" fill="#f7f8f9"/>
    <polygon points="600,30 830,230 600,430 370,230" fill="none" stroke="var(--panel-edge)" stroke-width="2"/>
    <polygon points="338,6 318,6 222,225 240,225" fill="var(--blue)"/>
    <polygon points="882,6 902,6 988,225 970,225" fill="var(--blue)"/>
    <polygon points="222,235 240,235 338,458 318,458" fill="var(--blue)"/>
    <polygon points="972,235 990,235 900,458 880,458" fill="var(--blue)"/>
  </svg>
  <div class="photo" role="img" aria-label="Photo of a large auditorium with rows of seats facing a stage" style="left:0;top:1617px;width:335px;height:220px;background:linear-gradient(160deg,#8f8a86,#4b4a4c 55%,#2f3033);clip-path:polygon(0 0,335px 0,240px 220px,0 220px)"></div>
  <div class="photo" role="img" aria-label="Photo of a home theater living room with a wall screen" style="left:885px;top:1617px;width:315px;height:220px;background:linear-gradient(160deg,#d8cdb6,#9b8466 55%,#c8b99a);clip-path:polygon(0 0,315px 0,315px 220px,100px 220px)"></div>
  <div class="photo" role="img" aria-label="Photo of a conference room with a long table and wall display" style="left:0;top:1847px;width:335px;height:223px;background:linear-gradient(160deg,#9a7b66,#5a4a40 50%,#bfb8b0);clip-path:polygon(0 0,222px 0,335px 223px,0 223px)"></div>
  <div class="photo" role="img" aria-label="Photo of a restaurant bar counter with stools" style="left:880px;top:1847px;width:320px;height:223px;background:linear-gradient(160deg,#3a3d42,#6b4e36 55%,#a37a4f);clip-path:polygon(110px 0,320px 0,320px 223px,0 223px)"></div>

  <div class="venue-label" style="left:285px;top:1705px;width:240px;background:var(--blue);clip-path:polygon(20px 0,240px 0,222px 47px,0 47px)">Auditorium</div>
  <div class="venue-label" style="left:673px;top:1705px;width:242px;background:var(--blue);clip-path:polygon(0 0,222px 0,242px 47px,18px 47px)">Home Theater</div>
  <div class="venue-label" style="left:270px;top:1939px;width:262px;background:var(--blue);clip-path:polygon(0 0,244px 0,262px 47px,20px 47px)">Conference Room</div>
  <div class="venue-label" style="left:667px;top:1939px;width:235px;background:var(--blue);clip-path:polygon(18px 0,235px 0,215px 47px,0 47px)">Restaurant</div>

  <div class="venue-brand">
    <div class="ring"></div>
    <div class="name">Brightfall<br>Systems</div>
  </div>

  <!-- footer -->
  <p class="disclaimer">Brightfall Systems designs, installs and programs audio, video and automation systems for residential and commercial clients. All product names, trademarks, and logos mentioned are property of their respective owners.</p>
  <div class="footer-rule"></div>
  <nav class="footer-nav"><span>Home</span>|<span>Contact Us</span>|<span>Service Support</span></nav>
  <p class="copyright">Copyright © 2017 Brightfall Systems. All Rights Reserved.</p>
  <div class="bottom-bar"></div>
</div>
</body>
</html>
```